Looking to Pick Up? Campaign

We are looking to design a double sided DL postcard to send to our clients to promote a new fixed cost recruitment service.
The theme of the campaign is to be 'Looking to Pick Up?'.
Attached is my own little mock up but I don't have the time or the skills to make something really impressionable.
Please note that the only things that need to be incorporated in this project from the draft that I've attached is the text (or similar) and our company logo.
if you need any royalty free mining pics or a gif of our logo, please email me, admin@stonecrewhq.com
Any questions, please ask.
Cheers
Brent
Updates
Dear Designers,
Please note that this design brief is for a double sided DL postcard. Some space must be left for a stamp & postage label on one side.
Secondly, the campaign is 'Looking to Pick Up', so risque / unique / memorable themes & graphics will be greatly appreciated.
Good luck!
Many thanks
Brent

```html
<!DOCTYPE html>
<html lang="en">
<head>
<meta charset="utf-8">
<title>Specialist Advertised &amp; Network Recruitment – Postcard</title>
<link rel="stylesheet" href="https://fonts.googleapis.com/css2?family=Anton&family=Arimo:wght@400;700&display=swap">
<style>
  :root {
    --paper: #ffffff;
    --ink-black: #0b0b0b;
    --panel-black: rgba(8, 8, 8, 0.92);
    --accent-yellow: #f2e52a;
    --text-white: #ffffff;
    --text-soft: #d8d8d8;
    --rule-grey: #c9c9c9;
    --stamp-line: #bdbdbd;
    --earth-dark: #3a332c;
    --earth-mid: #6b5d4f;
    --earth-light: #8c7f70;
  }
  html, body {
    margin: 0;
    padding: 0;
    overflow: hidden;
    background: var(--paper);
  }
  .postcard {
    position: relative;
    width: 1200px;
    height: 566px;
    background: var(--paper);
    overflow: hidden;
    font-family: "Arimo", Arial, sans-serif;
  }
  .mine-photo {
    position: absolute;
    left: 0;
    top: 0;
    width: 773px;
    height: 482px;
    background:
      radial-gradient(ellipse at 70% 20%, var(--earth-light) 0%, transparent 55%),
      radial-gradient(ellipse at 30% 90%, var(--earth-mid) 0%, transparent 60%),
      linear-gradient(160deg, var(--earth-mid) 0%, var(--earth-dark) 55%, #2a2520 100%);
  }
  .contact-strip {
    position: absolute;
    left: 36px;
    top: 0;
    width: 30px;
    height: 128px;
    background: var(--ink-black);
    border-radius: 0 0 15px 15px;
  }
  .contact-list {
    position: absolute;
    left: 44px;
    top: 16px;
    margin: 0;
    padding: 0;
    list-style: none;
    color: var(--text-white);
    font-weight: 700;
    font-size: 16.5px;
    line-height: 1.2;
  }
  .contact-list li {
    display: flex;
    align-items: flex-start;
    margin-bottom: 9px;
  }
  .contact-list svg {
    width: 14px;
    height: 14px;
    flex: none;
    margin-right: 16px;
    margin-top: 2px;
  }
  .offer-panel {
    position: absolute;
    left: 0;
    top: 150px;
    width: 760px;
    height: 315px;
  }
  .offer-content {
    position: absolute;
    left: 36px;
    top: 180px;
  }
  .headline {
    margin: 0;
    font-family: "Anton", Impact, sans-serif;
    font-weight: 400;
    color: var(--accent-yellow);
    font-size: 44px;
    line-height: 1.05;
    letter-spacing: 0.5px;
    text-shadow: 2px 2px 0 #000;
  }
  .price-list {
    margin: 10px 0 0;
    padding: 0;
    list-style: none;
    color: var(--text-white);
    font-size: 30px;
    line-height: 1.2;
  }
  .price {
    color: var(--accent-yellow);
    display: inline-block;
    min-width: 118px;
  }
  .price sup {
    font-size: 15px;
    vertical-align: 12px;
  }
  .upgrade-note {
    margin: 10px 0 0;
    color: var(--text-soft);
    font-size: 21.5px;
    line-height: 1.22;
  }
  .upgrade-note .price-inline {
    color: var(--accent-yellow);
  }
  .stamp-box {
    position: absolute;
    left: 999px;
    top: 15px;
    width: 176px;
    height: 183px;
    border: 1.5px solid var(--stamp-line);
    box-sizing: border-box;
  }
  .address-lines {
    position: absolute;
    left: 822px;
    top: 288px;
    width: 334px;
  }
  .address-lines span {
    display: block;
    height: 57px;
    border-top: 1.5px solid var(--rule-grey);
  }
</style>
</head>
<body>
  <div class="postcard">
    <div class="mine-photo" role="img" aria-label="Open-cut mine with terraced grey and brown pit walls and haul roads"></div>

    <div class="contact-strip"></div>
    <ul class="contact-list">
      <li>
        <svg viewBox="0 0 14 14"><path d="M7 1 L13 6.5 H11 V13 H8.5 V9 H5.5 V13 H3 V6.5 H1 Z" fill="#f2e52a"/></svg>
        <span>Level 3, 18 Quarry Lane, Red Hill,<br>Queensland, Australia 4059</span>
      </li>
      <li>
        <svg viewBox="0 0 14 14"><path d="M3 1 L5.5 1 L6.5 4.5 L5 5.8 C5.8 7.6 6.6 8.5 8.2 9.2 L9.5 7.7 L13 8.7 L13 11 C13 12 12 13 11 13 C6 12.5 1.5 8 1 3 C1 2 2 1 3 1 Z" fill="#f2e52a"/></svg>
        <span>+61 7 3000 4821</span>
      </li>
      <li>
        <svg viewBox="0 0 14 14" fill="none" stroke="#f2e52a" stroke-width="1.3"><circle cx="7" cy="7" r="5.8"/><ellipse cx="7" cy="7" rx="2.6" ry="5.8"/><path d="M1.2 7 H12.8 M2.3 4 H11.7 M2.3 10 H11.7"/></svg>
        <span>www.stonecrewhq.com</span>
      </li>
    </ul>

    <svg class="offer-panel" viewBox="0 0 760 315" aria-hidden="true">
      <polygon points="0,14 740,0 700,302 0,315" fill="rgba(8,8,8,0.92)"/>
    </svg>

    <div class="offer-content">
      <h1 class="headline">Specialist Advertised &amp;<br>Network Recruitment</h1>
      <ul class="price-list">
        <li><span class="price">$7K<sup>+GST*</sup></span> Roles up to AU$150K fixed remuneration</li>
        <li><span class="price">$12K<sup>+GST*</sup></span> Roles from AU$150K to AU$200K TFR</li>
      </ul>
      <p class="upgrade-note">Upgrade to premium ad package including Resource Times Professional<br>Placement &amp; CareerLink Job slot for only <span class="price-inline">$1600 + GST</span>.</p>
    </div>

    <div class="stamp-box" aria-label="Stamp area"></div>
    <div class="address-lines" aria-label="Address lines">
      <span></span><span></span><span></span><span></span>
    </div>
  </div>
</body>
</html>
```